Website for our 3rd party logistics warehouse company

Our company is a 3rd party logistics company. We receive and ship other businesses products for them. We offer our services to other smaller businesses that do not have a warehouse to operate out of. We also help many Brindlemart businesses prepare their products to be sold on Brindlemart.

We are looking for a modern looking design for our website. Please see our attached logo for design ideas. We are open to changing logo colors for website.

We really like the look of the website www.quorvane.com

Target Market(s)

Other businesses and brands of products

Industry/Entity Type

Warehousing and shipping

Number of Pages Required

2 page

Requirements
Must have
• We need 2 pages. Our main landing page and a duplicate page with different information geared towards brands.
Nice to have
• I like the look of overlay/transparent sections. Please see quorvane.com there is a ribbon that shows "Partners".

```html
<!DOCTYPE html>
<html lang="en">
<head>
<meta charset="utf-8">
<title>Orbitline 3PL — Warehousing &amp; Fulfilment</title>
<link rel="stylesheet" href="https://fonts.googleapis.com/css2?family=Krona+One&family=Roboto:wght@400;500;700&display=swap">
<style>
:root{
  --gold:#fbc02d;
  --gold-deep:#f5b50f;
  --ink:#111111;
  --text:#2b2b2b;
  --muted:#6b6b6b;
  --line:#d9d9d9;
  --white:#ffffff;
  --black:#050505;
  --field:#c9c9c9;
  --display:"Krona One",sans-serif;
  --body:"Roboto",sans-serif;
}
*{box-sizing:border-box;margin:0;padding:0}
html,body{width:1200px;height:4488px;overflow:hidden}
body{position:relative;font-family:var(--body);color:var(--text);background:var(--white)}
.abs{position:absolute}
.display{font-family:var(--display);text-transform:uppercase;letter-spacing:1px;color:var(--ink)}
.display .accent{color:var(--gold)}
.btn{position:absolute;display:flex;align-items:center;justify-content:center;border-radius:30px;font-weight:500;font-size:15px;text-transform:uppercase;color:var(--ink)}
.btn-gold{background:var(--gold)}
.btn-outline{border:2px solid var(--ink)}
.wordmark{font-family:var(--display);text-transform:uppercase;display:flex;align-items:center;gap:10px}
.wordmark .dot{width:14px;height:14px;border-radius:50%;background:var(--gold)}

/* hero */
.hero{position:absolute;left:0;top:0;width:1200px;height:630px;overflow:hidden}
.hero-photo{position:absolute;inset:0;background:linear-gradient(160deg,#3d4a33 0%,#5b6748 30%,#7c7f70 55%,#4f5a44 75%,#2f3a2a 100%)}
.hero-shade{position:absolute;inset:0;background:linear-gradient(90deg,rgba(0,0,0,.45),rgba(0,0,0,.05) 60%)}
.hero .logo{left:99px;top:44px;color:var(--white);font-size:20px}
.nav{position:absolute;top:38px;left:0;width:1200px}
.nav a{position:absolute;color:var(--white);font-size:15px;text-decoration:none;font-weight:500}
.call{position:absolute;left:935px;top:28px;display:flex;align-items:center;gap:12px;color:var(--white)}
.call .ring{width:38px;height:38px;border-radius:50%;background:var(--gold);display:flex;align-items:center;justify-content:center}
.call small{display:block;font-size:10px;font-weight:500}
.call strong{font-size:15px;font-weight:500}
.hero h1{position:absolute;left:127px;top:200px;color:var(--white);font-size:35px;line-height:52px;font-weight:400}
.hero .btn{left:127px;top:377px;width:190px;height:50px}
.arrow{position:absolute;top:300px}
.partners{position:absolute;left:0;top:528px;width:1200px;height:102px;background:rgba(0,0,0,.55)}
.partners .label{position:absolute;left:99px;top:8px;color:var(--gold);font-size:17px;text-decoration:underline}
.partner{position:absolute;top:44px;color:var(--white);font-family:var(--body);font-weight:700;font-size:27px;display:flex;align-items:center;gap:10px}
.partner .mark{width:28px;height:28px;border-radius:50%;background:var(--white)}

/* about */
.about{position:absolute;left:99px;top:718px;width:1002px;height:449px;background:var(--white);box-shadow:0 2px 14px rgba(0,0,0,.12);border-radius:4px;overflow:hidden}
.about-photo{position:absolute;left:0;top:0;width:520px;height:449px;background:linear-gradient(135deg,#cfd6d8 0%,#8d9ba3 40%,#5a6f86 70%,#3a4756 100%)}
.about h2{position:absolute;left:561px;top:98px;font-size:32px}
.about p{position:absolute;left:561px;top:152px;width:390px;font-size:14px;line-height:29px;color:var(--text)}
.about .btn{left:561px;top:297px;width:188px;height:50px}

/* why */
.why-title{position:absolute;left:0;top:1255px;width:1200px;text-align:center;font-size:32px}
.why-rule{position:absolute;top:1275px;height:1px;background:var(--line);width:186px}
.feature{position:absolute;top:1339px;width:230px;text-align:center}
.feature .badge{width:122px;height:122px;border-radius:50%;background:var(--gold);margin:0 auto 22px;display:flex;align-items:center;justify-content:center}
.feature p{font-size:15.5px;line-height:26px;color:var(--ink)}
.why-base{position:absolute;left:99px;top:1628px;width:1002px;height:1px;background:var(--line)}

/* guarantee */
.guarantee{position:absolute;left:0;top:1723px;width:1200px;height:549px;overflow:hidden;border-top-right-radius:120px}
.guarantee-photo{position:absolute;inset:0;background:linear-gradient(90deg,#c9a35a 0%,#b99860 25%,#6d7d92 55%,#4b5a6e 75%,#8a95a0 100%)}
.guarantee h2{position:absolute;left:190px;top:128px;font-size:31px;line-height:35px}
.guarantee p{position:absolute;left:190px;top:212px;width:340px;font-size:13px;line-height:27px;color:var(--ink)}
.guarantee .btn{left:190px;top:373px;width:188px;height:50px}

/* software */
.laptop{position:absolute;left:99px;top:2366px;width:512px;height:270px;background:linear-gradient(180deg,#1d1d1f 0%,#2f3035 82%,#b9bbbf 84%,#e4e5e7 100%);border-radius:10px 10px 4px 4px}
.software h2{position:absolute;left:660px;top:2410px;font-size:30px}
.software p{position:absolute;left:660px;top:2455px;width:420px;font-size:15px;line-height:31px;color:var(--text)}

/* benefits */
.benefits{position:absolute;left:0;top:2731px;width:1200px;height:697px;background:radial-gradient(ellipse at 60% 60%,#1c1c1c 0%,var(--black) 70%);border-top-left-radius:120px;overflow:hidden}
.benefits h2{position:absolute;left:0;top:98px;width:1200px;text-align:center;color:var(--white);font-size:32px}
.benefit{position:absolute;color:var(--white);font-size:17px;font-weight:500}

/* contact */
.contact{position:absolute;left:0;top:3428px;width:1200px;height:688px;background:#f6f6f6}
.contact h2{position:absolute;left:0;top:98px;width:1200px;text-align:center;font-size:32px}
.info{position:absolute;top:186px;display:flex;gap:14px;font-size:14px;line-height:19px;color:var(--ink)}
.info .ring{width:46px;height:46px;border-radius:50%;border:2px solid var(--gold);display:flex;align-items:center;justify-content:center;flex:none;background:var(--white)}
.field{position:absolute;width:371px;height:61px;background:var(--white);border:1px solid var(--field);padding:20px;font-size:15px;color:var(--muted)}
.contact .btn{left:497px;top:552px;width:206px;height:48px;font-size:16px;font-weight:700}

/* footer */
.footer{position:absolute;left:0;top:4116px;width:1200px;height:372px;background:#0b0b0b;color:var(--white)}
.footer .logo{left:103px;top:170px;font-size:28px;color:var(--white)}
.footer h4{position:absolute;font-size:16px;font-weight:700;letter-spacing:.5px}
.footer .news{position:absolute;left:436px;top:86px;width:280px;font-size:13px;line-height:22px}
.footer .email{position:absolute;left:436px;top:183px;width:273px;height:38px;background:var(--white);color:#888;font-size:12px;padding:11px 16px}
.footer .btn{left:436px;top:240px;width:134px;height:34px;font-size:14px;font-weight:700}
.footer ul{position:absolute;list-style:none;font-size:13px;line-height:28.5px}
.social li{display:flex;align-items:center;gap:10px}
.social .circ{width:22px;height:22px;border-radius:50%;border:1.5px solid var(--white)}
.copyright{position:absolute;left:0;top:4441px;width:1200px;text-align:center;color:var(--white);font-size:14px}
</style>
</head>
<body>

<!-- hero -->
<header class="hero">
  <div class="hero-photo" role="img" aria-label="Photo of a white cargo truck on a winding mountain highway through pine forest"></div>
  <div class="hero-shade"></div>
  <div class="abs wordmark logo"><span class="dot"></span>Orbitline 3PL</div>
  <nav class="nav">
    <a style="left:415px">HOME</a>
    <a style="left:498px">ABOUT US</a>
    <a style="left:608px">SERVICES</a>
    <a style="left:716px">SOFTWARE</a>
    <a style="left:833px">CONTACT</a>
  </nav>
  <div class="call">
    <span class="ring"><svg width="18" height="18" viewBox="0 0 24 24"><path d="M6.6 10.8a15 15 0 0 0 6.6 6.6l2.2-2.2c.3-.3.7-.4 1-.2 1.1.4 2.3.6 3.6.6.6 0 1 .4 1 1V20c0 .6-.4 1-1 1A17 17 0 0 1 3 4c0-.6.4-1 1-1h3.5c.6 0 1 .4 1 1 0 1.3.2 2.5.6 3.6.1.3 0 .7-.2 1z" fill="#111"/></svg></span>
    <div><small>GIVE US A CALL</small><strong>+(555) 014-2290</strong></div>
  </div>
  <svg class="arrow" style="left:60px" width="24" height="40" viewBox="0 0 24 40"><path d="M20 2 4 20l16 18" stroke="#fff" stroke-width="2" fill="none"/></svg>
  <svg class="arrow" style="left:1108px" width="24" height="40" viewBox="0 0 24 40"><path d="M4 2l16 18L4 38" stroke="#fff" stroke-width="2" fill="none"/></svg>
  <h1 class="display">Grow your<br>business with<br>Orbitline 3PL</h1>
  <a class="btn btn-gold">Get started</a>
  <div class="partners">
    <span class="label">Partners</span>
    <div class="partner" style="left:99px"><span class="mark"></span>Halvard</div>
    <div class="partner" style="left:405px;font-size:21px"><span class="mark"></span>Fennick</div>
    <div class="partner" style="left:644px">Mailcrest</div>
    <div class="partner" style="left:882px"><span class="mark"></span>Tessaro</div>
  </div>
</header>

<!-- who we are -->
<section class="about">
  <div class="about-photo" role="img" aria-label="Photo of a smiling truck driver seated at the wheel of his cab"></div>
  <svg class="abs" style="left:0;top:0" width="620" height="449" viewBox="0 0 620 449">
    <path d="M520 0Q620 180 530 330 480 410 420 449L620 449 620 0Z" fill="#fff"/>
    <path d="M430 0Q560 120 510 300 480 400 420 449" stroke="#fbc02d" stroke-width="3" fill="none"/>
  </svg>
  <h2 class="display">Who we <span class="accent">are</span></h2>
  <p>Orbitline 3PL is your one stop 3PL that will help you grow your business and allow you to be hands off. We offer high end services and meet our commitment, guaranteed.</p>
  <a class="btn btn-gold">Learn more</a>
</section>

<!-- why -->
<section>
  <div class="why-rule" style="left:99px"></div>
  <div class="why-rule" style="left:915px"></div>
  <h2 class="display why-title">Why use a <span class="accent">prep 3PL?</span></h2>
  <div class="feature" style="left:98px">
    <div class="badge"><svg width="70" height="70" viewBox="0 0 70 70" fill="none" stroke="#111" stroke-width="2.5"><circle cx="35" cy="35" r="27"/><path d="M18 20c6 2 8 8 14 8s4 8 0 10-6 8-3 14M40 10c-2 6 4 8 8 6s10 6 6 12-8 4-6 12"/></svg></div>
    <p>Work from anywhere in the world.</p>
  </div>
  <div class="feature" style="left:357px">
    <div class="badge"><svg width="70" height="70" viewBox="0 0 70 70" fill="none" stroke="#111" stroke-width="2.5"><circle cx="35" cy="24" r="9"/><path d="M35 8v4M35 36v4M19 24h4M47 24h4M12 50l12-8 12 6 12-6 12 8M20 56l10-6M40 56l10-6"/></svg></div>
    <p>Don't have to manage employees, health insurance plans, payroll, sick calls, etc.</p>
  </div>
  <div class="feature" style="left:617px">
    <div class="badge"><svg width="70" height="70" viewBox="0 0 70 70" fill="none" stroke="#111" stroke-width="2.5"><path d="M35 6l7 5 9-1 2 9 7 6-4 8 4 8-7 5-2 9-9-1-7 5-7-5-9 1-2-9-7-5 4-8-4-8 7-6 2-9 9 1z"/><path d="M24 34l8 8 14-15"/></svg></div>
    <p>Don't get locked into a 3-5 year warehouse lease where you guarantee hundreds of thousands of dollars</p>
  </div>
  <div class="feature" style="left:876px">
    <div class="badge"><svg width="70" height="70" viewBox="0 0 70 70" fill="none" stroke="#111" stroke-width="2.5"><path d="M10 58h52M16 58V44h8v14M30 58V36h8v22M44 58V28h8v30M12 36l14-12 10 6 20-16M48 14h8v8"/></svg></div>
    <p>Grow your business without commitment</p>
  </div>
  <div class="why-base"></div>
</section>

<!-- guarantee -->
<section class="guarantee">
  <div class="guarantee-photo" role="img" aria-label="Photo of two warehouse workers in high-visibility vests checking a parcel between storage racks"></div>
  <svg class="abs" style="left:0;top:0" width="1200" height="549" viewBox="0 0 1200 549">
    <path d="M0 0H218L0 330Z" fill="#fbc02d" opacity=".55"/>
    <path d="M218 0H732L545 549H0V330Z" fill="#fbc02d"/>
  </svg>
  <h2 class="display">Our<br>guarantee</h2>
  <p>All orders will be prepped and ready for shipment in 48 business hours (often 24 or less) and we guarantee it. We are confident in our services and if we do not fulfill our obligation, we offer a 500 item (up to $700) credit on your next shipment.</p>
  <a class="btn btn-outline">Contact us</a>
</section>

<!-- software -->
<section class="software">
  <div class="laptop" role="img" aria-label="Laptop showing the inventory dashboard with charts and order status"></div>
  <h2 class="display">Our <span class="accent">software</span></h2>
  <p>Know what inventory is at our warehouse in real time. Our software allows you to track your inventory and know how your shipment status in real time. Professional software designed specifically for our needs.</p>
</section>

<!-- benefits -->
<section class="benefits">
  <h2 class="display">Our benefits</h2>
  <svg class="abs" style="left:0;top:0" width="1200" height="697" viewBox="0 2731 1200 697" fill="none">
    <circle cx="279" cy="3136" r="153" stroke="#fbc02d" stroke-width="5"/>
    <path d="M384 2954A210 210 0 0 1 414 3297" stroke="#fbc02d" stroke-width="4"/>
    <path d="M330 2935A210 210 0 0 1 384 2954M414 3297A210 210 0 0 1 330 3340" stroke="#fbc02d" stroke-width="2"/>
    <g stroke="#cfcfcf" stroke-width="1.5">
      <path d="M425 2985L445 2960H500"/>
      <path d="M474 3057L500 3028H554"/>
      <path d="M488 3121H625"/>
      <path d="M483 3187L510 3205H611"/>
      <path d="M444 3265L470 3310H515"/>
    </g>
    <g fill="#fbc02d">
      <circle cx="425" cy="2985" r="8"/><circle cx="474" cy="3057" r="8"/><circle cx="488" cy="3121" r="8"/><circle cx="483" cy="3187" r="8"/><circle cx="444" cy="3265" r="8"/>
    </g>
    <g fill="#fff" stroke="#fbc02d" stroke-width="3">
      <circle cx="530" cy="2960" r="30"/><circle cx="584" cy="3028" r="30"/><circle cx="655" cy="3121" r="30"/><circle cx="641" cy="3205" r="30"/><circle cx="545" cy="3310" r="30"/>
    </g>
    <g stroke="#111" stroke-width="2">
      <circle cx="530" cy="2960" r="13"/><path d="M524 2960l4 4 8-8"/>
      <rect x="574" y="3017" width="16" height="20"/><path d="M578 3023h8M578 3028h8M578 3033h5"/><circle cx="593" cy="3036" r="5"/>
      <rect x="643" y="3112" width="24" height="14"/><circle cx="655" cy="3119" r="3"/>
      <rect x="630" y="3200" width="22" height="14"/><path d="M636 3200v-6h10v6"/>
      <circle cx="545" cy="3305" r="7"/><path d="M533 3322c2-6 6-9 12-9s10 3 12 9"/>
    </g>
  </svg>
  <div class="abs wordmark" style="left:160px;top:394px;font-size:26px;color:var(--white)">Orbitline 3PL</div>
  <div class="benefit" style="left:574px;top:218px">48 hour turn around guarantee – done in 48 hours or its free*</div>
  <div class="benefit" style="left:628px;top:286px">No monthly subscription – only pay for what you use</div>
  <div class="benefit" style="left:699px;top:380px">No receiving fees</div>
  <div class="benefit" style="left:685px;top:463px">No pallet or outbound fees</div>
  <div class="benefit" style="left:589px;top:568px">Email and phone support</div>
</section>

<!-- contact -->
<section class="contact">
  <h2 class="display">Get in <span class="accent">touch</span></h2>
  <div class="info" style="left:222px">
    <span class="ring"><svg width="20" height="20" viewBox="0 0 24 24"><path d="M12 2a7 7 0 0 0-7 7c0 5 7 13 7 13s7-8 7-13a7 7 0 0 0-7-7zm0 9.5A2.5 2.5 0 1 1 12 6.5a2.5 2.5 0 0 1 0 5z" fill="#111"/></svg></span>
    <div>ORBITLINE 3PL<br>48 Corvel Lane Westbrook<br>USA 20417</div>
  </div>
  <div class="info" style="left:551px">
    <span class="ring"><svg width="20" height="20" viewBox="0 0 24 24"><path d="M6.6 10.8a15 15 0 0 0 6.6 6.6l2.2-2.2c.3-.3.7-.4 1-.2 1.1.4 2.3.6 3.6.6.6 0 1 .4 1 1V20c0 .6-.4 1-1 1A17 17 0 0 1 3 4c0-.6.4-1 1-1h3.5c.6 0 1 .4 1 1 0 1.3.2 2.5.6 3.6.1.3 0 .7-.2 1z" fill="#111"/></svg></span>
    <div>Phone<br>+555 014 2290</div>
  </div>
  <div class="info" style="left:783px">
    <span class="ring"><svg width="20" height="20" viewBox="0 0 24 24"><path d="M3 6h18v12H3z" fill="#111"/><path d="M3 6l9 7 9-7" stroke="#fff" stroke-width="1.6" fill="none"/></svg></span>
    <div>Email<br>info@tarnwell.com</div>
  </div>
  <div class="field" style="left:214px;top:291px">Your name</div>
  <div class="field" style="left:613px;top:291px">Company</div>
  <div class="field" style="left:214px;top:373px">Email address</div>
  <div class="field" style="left:613px;top:373px;height:143px">Message</div>
  <div class="field" style="left:214px;top:455px">Phone</div>
  <a class="btn btn-gold">Submit</a>
</section>

<!-- footer -->
<footer class="footer">
  <div class="abs wordmark logo"><span class="dot"></span>Orbitline 3PL</div>
  <h4 style="left:436px;top:52px">SIGN UP FOR NEWSLETTER</h4>
  <p class="news">Excepteur sint occaecat cupidatat non proident, sunt in culpa qui officia deserunt</p>
  <div class="email">Enter email</div>
  <a class="btn btn-gold">Subscribe</a>
  <h4 style="left:766px;top:47px">QUICK LINKS</h4>
  <ul style="left:770px;top:76px"><li>Home</li><li>About Us</li><li>Services</li><li>Software</li><li>Contact</li></ul>
  <h4 style="left:958px;top:49px">FOLLOW US</h4>
  <ul class="social" style="left:958px;top:80px;line-height:34px">
    <li><span class="circ"></span>Chatterly</li>
    <li><span class="circ"></span>Quillpost</li>
    <li><span class="circ"></span>Orbnet</li>
    <li><span class="circ"></span>Reelcast</li>
  </ul>
</footer>
<p class="copyright">© 2021 ORBITLINE 3PL . All Rights Reserved</p>

</body>
</html>
```